依頼詳細
発泡スチロール製品の事例を紹介するリーフレットのデザインをお願い致します。
発泡スチロールの箱をいろいろな業種の方にご利用いただいております。いろいろな発泡スチロールの利用状況とお客様の声を今後DMとして発送を計画しております。
シリーズとして使えるようにしていきたいと考えております。今回は緑系統で、今後は色を替えることも想定してデザインをお願いできればと思います。
記載項目
社名、電話番号、ホームページアドレス、所在地
サイズ
A4
ページ数
片面
希望イメージ
シンプル 複雑
単色 カラフル
暗い 明るい
日常 高級
遊び心 厳粛
未来的 伝統的
女性的 男性的
希望する色
緑系、ロゴの色
納品ファイル
• イラストレーター形式 (.ai)
補足説明
ロゴデータはありません。添付書類参照下さい。
お世話になっております。コンペ参加者の皆様大変申し訳ありませんが、もう少し提案数が必要なため提案期日を10日延長いたしました。
現在参加されている方には大変申し訳ありませんがご理解いただきますようお願い申し上げます。
■ 選んだ理由

大変素晴らしいデザインありがとうございました。
お客様も大変悩まれておりましたが、大変気に入って頂けました。

■ 提案者全員のお礼・コメント

沢山のご提案ありがとうございました。
今後共デザインコンペを行ってまいりますのでよろしくお願いいたします。

```html
<!DOCTYPE html>
<html lang="ja">
<head>
<meta charset="utf-8">
<title>販売事例 アイス保冷用発泡スチロール</title>
<link href="https://fonts.googleapis.com/css2?family=Noto+Sans+JP:wght@400;500;700;900&display=swap" rel="stylesheet">
<style>
:root{
  --green-dark:#1f7a36;
  --green:#3a9d3f;
  --green-light:#8cc63f;
  --green-pale:#e6f2d8;
  --green-mist:#f3f9ec;
  --accent:#e8542a;
  --yellow:#ffe14a;
  --ink:#333333;
  --white:#ffffff;
  --brown:#8b6a43;
}
*{margin:0;padding:0;box-sizing:border-box}
html,body{width:846px;height:1200px;overflow:hidden}
body{font-family:"Noto Sans JP",sans-serif;color:var(--ink);background:var(--white)}
.sheet{position:relative;width:846px;height:1200px;overflow:hidden;background:var(--white)}

.header{position:absolute;left:0;top:0;width:846px;height:150px;
  background:linear-gradient(180deg,var(--green-pale) 0%,var(--white) 100%)}
.header .band{position:absolute;left:0;top:58px;width:846px;height:78px;
  background:linear-gradient(90deg,var(--green-dark),var(--green) 50%,var(--green-light))}
.header .tag{position:absolute;left:298px;top:12px;width:250px;height:54px;border-radius:27px;
  background:var(--green-dark);color:var(--white);font-size:32px;font-weight:900;
  text-align:center;line-height:54px;letter-spacing:4px;border:3px solid var(--white);z-index:2}
.header h1{position:absolute;left:0;top:68px;width:846px;text-align:center;color:var(--white);
  font-size:46px;font-weight:900;letter-spacing:2px;line-height:60px}

.request{position:absolute;left:0;top:150px;width:846px;height:280px;
  background:linear-gradient(160deg,var(--green-mist) 0%,var(--green-pale) 100%)}
.request .client{position:absolute;left:28px;top:20px;width:112px;height:112px;border-radius:50%;
  background:linear-gradient(180deg,#dfe7e0,#b9c7bb);border:4px solid var(--white)}
.request .intro{position:absolute;left:160px;top:28px;width:640px;color:var(--green-dark);
  font-size:16px;font-weight:700;line-height:1.8}
.request .label{position:absolute;left:18px;top:140px;padding:4px 14px;border-radius:14px;
  background:var(--green-dark);color:var(--white);font-size:13px;font-weight:700}
.needs{position:absolute;left:190px;top:112px;width:640px;height:160px}
.need{position:absolute;width:178px;height:150px;border-radius:50%;background:var(--white);
  box-shadow:0 2px 6px rgba(0,0,0,.12);display:flex;align-items:center;justify-content:center;
  text-align:center;font-size:14px;font-weight:500;line-height:1.6;padding:18px}
.need .num{position:absolute;top:-6px;left:70px;width:34px;height:34px;border-radius:50%;
  background:var(--accent);color:var(--white);font-weight:900;font-size:18px;line-height:34px;text-align:center}
.need.one{left:0;top:6px}
.need.two{left:205px;top:0}
.need.three{left:420px;top:6px}

.proposal{position:absolute;left:0;top:430px;width:846px;height:230px}
.proposal .badge{position:absolute;left:14px;top:10px;width:160px;height:160px;border-radius:50%;
  background:var(--green);color:var(--white);text-align:center;padding:26px 16px}
.proposal .badge h2{font-size:15px;font-weight:900;line-height:1.3;border-bottom:1px solid rgba(255,255,255,.6);padding-bottom:6px;margin-bottom:6px}
.proposal .badge p{font-size:11px;line-height:1.55}
.photo{position:absolute;top:0;height:190px;border-radius:6px}
.photo.cups{left:188px;width:275px;background:linear-gradient(160deg,#f4f1ea,#cfc7b6)}
.photo.box{left:478px;width:350px;background:linear-gradient(160deg,#e9dcc6,var(--brown))}
.burst{position:absolute;top:150px;width:74px;height:74px}
.burst span{position:absolute;inset:0;display:flex;align-items:center;justify-content:center;
  color:var(--accent);font-size:17px;font-weight:900}
.burst.a{left:180px}.burst.b{left:470px}
.caption{position:absolute;top:196px;font-size:12.5px;font-weight:700;line-height:1.5;color:var(--ink)}
.caption.a{left:258px;width:200px}
.caption.b{left:548px;width:280px}

.voice{position:absolute;left:20px;top:672px;width:806px;height:272px;border:2px solid var(--green);
  border-radius:10px;background:var(--white)}
.voice h3{position:absolute;left:14px;top:-16px;background:var(--green);color:var(--white);
  font-size:15px;font-weight:700;padding:4px 18px;border-radius:15px}
.voice p{position:absolute;left:22px;top:26px;width:762px;font-size:15.5px;line-height:2.05;color:var(--ink)}
.voice p u{text-decoration-color:var(--accent)}

.wave{position:absolute;left:0;top:950px;width:846px;height:145px}

.footer{position:absolute;left:0;top:1095px;width:846px;height:105px}
.footer .tagline{position:absolute;left:30px;top:0;font-size:16px;font-weight:700;color:var(--green-dark)}
.footer .company{position:absolute;left:30px;top:18px;font-size:36px;font-weight:900;color:var(--green-dark);letter-spacing:1px;line-height:52px}
.footer .address{position:absolute;left:30px;top:72px;font-size:10.5px;line-height:1.4;color:var(--ink)}
.footer .contact-label{position:absolute;left:480px;top:0;font-size:13px;font-weight:700;color:var(--green-dark)}
.footer .phone{position:absolute;left:470px;top:16px;display:flex;align-items:center;gap:8px;
  font-size:40px;font-weight:900;color:var(--green-dark);line-height:52px}
.footer .web{position:absolute;left:470px;top:72px;width:350px;height:26px;border-radius:13px;
  background:var(--green);color:var(--white);font-size:15px;font-weight:700;line-height:26px;padding-left:20px}
</style>
</head>
<body>
<div class="sheet">

  <header class="header">
    <div class="band"></div>
    <div class="tag">販売事例</div>
    <h1>アイス保冷用発泡スチロール</h1>
  </header>

  <section class="request">
    <div class="client" role="img" aria-label="依頼者のイラスト"></div>
    <p class="intro">新商品のアイスクリームを開発中、そのアイスクリームは生乳やバニラなど素材にこだわった、今までに無い高級なアイスクリームを販売したい。</p>
    <span class="label">お客様からのご要望</span>
    <div class="needs">
      <div class="need one"><span class="num">1</span>名前は「翠涼アイス」。3個入りの発泡スチロール容器が必要。</div>
      <div class="need two"><span class="num">2</span>販売数量は特別品のため、それほど多くはないので型代などの経費はかけられない。</div>
      <div class="need three"><span class="num">3</span>保冷性能が高く外観も高級感を持ったパッケージを使用したい。</div>
    </div>
  </section>

  <section class="proposal">
    <div class="badge">
      <h2>ミドリパック<br>のご提案</h2>
      <p>既存の型を使い、色を変えて高級感のあるパッケージをご提案しました。</p>
    </div>
    <div class="photo cups" role="img" aria-label="カップを収めた発泡スチロール容器の写真"></div>
    <div class="photo box" role="img" aria-label="ブラウンの発泡スチロール箱の写真"></div>
    <div class="burst a">
      <svg viewBox="0 0 100 100" width="74" height="74"><polygon fill="var(--yellow)" points="50,0 60,22 82,12 76,36 100,42 80,58 94,78 70,76 66,100 50,84 34,100 30,76 6,78 20,58 0,42 24,36 18,12 40,22"/></svg>
      <span>解決</span>
    </div>
    <div class="burst b">
      <svg viewBox="0 0 100 100" width="74" height="74"><polygon fill="var(--yellow)" points="50,0 60,22 82,12 76,36 100,42 80,58 94,78 70,76 66,100 50,84 34,100 30,76 6,78 20,58 0,42 24,36 18,12 40,22"/></svg>
      <span>解決</span>
    </div>
    <p class="caption a">今回は社既製品から一番良いと思われる製品を選定！</p>
    <p class="caption b">外観については高級感を出せるカラーのブラウン製品を選定！</p>
  </section>

  <section class="voice">
    <h3>お客様からの声</h3>
    <p>「発泡スチロール容器が白色では台無し（高級感が無い）」とのお考えがあり、提案したサンプルが「翠涼アイス」の<u>コンセプト</u>に合致していた。提案としてはアイス発泡スチロール容器が<u>茶色の素材感</u>を感じられる点、中仕切りは黒色でブラウンとマッチして<u>高級感が感じられ</u>「翠涼アイス」のこだわりを表現できる点が評価され、決定となった。上記のような説明を受けました。また本部長の皆様から「今回の採用は、ミドリパックからの<u>細かな対応力が決め手</u>となった」とのお言葉も頂けました。</p>
  </section>

  <svg class="wave" viewBox="0 0 846 145" preserveAspectRatio="none" aria-hidden="true">
    <path d="M0 45 C200 5 420 95 846 25 L846 145 L0 145 Z" fill="var(--green-pale)"/>
    <path d="M0 90 C260 50 520 130 846 70 L846 145 L0 145 Z" fill="var(--green-light)" opacity=".55"/>
  </svg>

  <footer class="footer">
    <p class="tagline">品質に自信と誇り</p>
    <p class="company">株式会社ミドリパック</p>
    <p class="address">〒123-4567<br>緑野県若葉市青葉町1-2-3　FAX 0289-00-1235</p>
    <p class="contact-label">お問い合わせは</p>
    <p class="phone">
      <svg width="34" height="34" viewBox="0 0 24 24" aria-hidden="true"><path fill="var(--green-dark)" d="M6.6 10.8a15.1 15.1 0 0 0 6.6 6.6l2.2-2.2c.3-.3.7-.4 1-.2 1.1.4 2.3.6 3.6.6.6 0 1 .4 1 1V20c0 .6-.4 1-1 1A17 17 0 0 1 3 4c0-.6.4-1 1-1h3.5c.6 0 1 .4 1 1 0 1.3.2 2.5.6 3.6.1.3 0 .7-.2 1z"/></svg>
      0289-00-1234
    </p>
    <p class="web">https://www.midoripack.example/</p>
  </footer>

</div>
</body>
</html>
```